Custom workshop/manufacture for custom furniture, architectural millwork and kitchen cabinetry

simple and clean. I like this website:
http://www.pebblelarchworks.com

Attached are random ideas

Target Market(s)

residential, commercial, hospitality, interior designers, architects, contractors

Coding

Coded - Design and coding required

Number of Pages Required

5+ page

Font styles to use
Other font styles liked:
• Avenir next

Requirements
Must have
• drop down menu for work - residential - commercial

```html
<!DOCTYPE html>
<html lang="en">
<head>
<meta charset="utf-8">
<title>Harlow Custom Furniture</title>
<link href="https://fonts.googleapis.com/css2?family=Playfair+Display:wght@400&family=Open+Sans:wght@400&display=swap" rel="stylesheet">
<style>
:root{
  --ink:#222;
  --text:#444;
  --muted:#666;
  --white:#fff;
  --nav:#333;
  --nav-active:#555;
  --band:#f0f0f0;
  --band-dark:#e6e6e6;
  --footer:#333;
  --line:#888;
}
*{margin:0;padding:0;box-sizing:border-box}
html,body{width:1200px;height:2679px;overflow:hidden}
body{position:relative;background:var(--white);color:var(--text);font-family:'Open Sans',sans-serif}
.abs{position:absolute}
.serif{font-family:'Playfair Display',serif}

.site-header{left:0;top:0;width:1200px;height:80px;background:var(--white)}
.brand{left:132px;top:20px;display:flex;align-items:center;gap:14px;font-family:'Playfair Display',serif;font-size:32px;color:var(--ink)}
.brand-mark{width:30px;height:30px;background:var(--ink)}
.header-phone{right:132px;top:24px;font-size:24px;color:var(--muted);display:flex;align-items:center;gap:8px}

.main-nav{left:0;top:80px;width:1200px;height:41px;background:var(--nav)}
.nav-item{position:absolute;top:0;height:41px;line-height:41px;font-family:'Playfair Display',serif;font-size:13px;color:var(--white);text-transform:uppercase;transform:translateX(-50%);white-space:nowrap}
.nav-active{left:132px;top:0;width:133px;height:41px;background:var(--nav-active)}

.hero{left:0;top:121px;width:1200px;height:494px;background:linear-gradient(100deg,#e9e8e6 0%,#d9d6d2 35%,#b8aea6 55%,#7a4a35 80%,#4a2a1e 100%)}
.hero-caption{left:425px;top:316px;width:348px;height:104px;background:rgba(255,255,255,.72);display:flex;align-items:center;justify-content:center;text-align:center;font-family:'Playfair Display',serif;font-size:30px;line-height:38px;color:var(--ink);text-transform:uppercase}
.hero-arrow{top:355px;width:28px;height:28px;background:var(--ink);display:flex;align-items:center;justify-content:center}

h2{font-family:'Playfair Display',serif;font-weight:400;color:var(--ink);text-transform:uppercase}
.welcome-title{left:132px;top:688px;font-size:31px;line-height:41px}
.body-copy{font-size:13px;line-height:25.5px;color:var(--text)}
.welcome-copy{left:132px;top:780px;width:470px}
.btn{display:inline-block;border:1px solid var(--line);font-family:'Playfair Display',serif;font-size:13px;color:var(--ink);padding:0 12px;height:35px;line-height:33px;background:var(--white)}
.welcome-photo{left:632px;top:697px;width:436px;height:286px;background:linear-gradient(135deg,#8a6a45,#d8b78c 45%,#caa476 70%,#6f5a48)}

.service-band{top:1066px;height:405px}
.service-icon{width:64px;height:64px}
.service-title{font-size:31px;line-height:40px}
.service-copy{width:430px}

.gallery-title{left:0;width:1200px;top:1540px;text-align:center;font-size:31px}
.tile{position:absolute}
.gallery-arrow{top:1756px;width:24px;height:30px}

.reviews{left:0;top:2026px;width:1200px;height:343px;background:var(--band)}
.reviews-title{left:0;width:1200px;top:2116px;text-align:center;font-size:31px}
.quote{left:140px;width:920px;top:2154px;text-align:center;font-family:'Playfair Display',serif;font-size:19px;line-height:29px;color:var(--ink)}
.reviewer{left:0;width:1200px;top:2222px;text-align:center;font-family:'Playfair Display',serif;font-size:19px;color:var(--ink)}
.dots{left:0;width:1200px;top:2274px;display:flex;justify-content:center;gap:16px}
.dot{width:16px;height:16px;border-radius:50%;background:#aaa}
.dot.on{background:var(--ink)}

.contact-title{left:0;width:1200px;top:2440px;text-align:center;font-size:31px}
.contact-item{top:2494px;display:flex;align-items:center;gap:8px;font-family:'Playfair Display',serif;font-size:17px;color:var(--ink)}

.site-footer{left:0;top:2579px;width:1200px;height:100px;background:var(--footer);color:var(--white)}
.footer-links{left:132px;top:2606px;font-size:11px}
.footer-links span{margin:0 6px}
.copyright{left:132px;top:2631px;font-size:11px}
.social{top:2619px;width:18px;height:18px;border-radius:50%;background:var(--white)}
</style>
</head>
<body>

<header class="abs site-header">
  <div class="abs brand"><span class="brand-mark"></span>Harlow Custom Furniture</div>
  <div class="abs header-phone">
    <svg width="18" height="18" viewBox="0 0 24 24"><path fill="#666" d="M6.6 10.8c1.4 2.8 3.8 5.1 6.6 6.6l2.2-2.2c.3-.3.7-.4 1-.2 1.1.4 2.3.6 3.6.6.6 0 1 .4 1 1V20c0 .6-.4 1-1 1C10.6 21 3 13.4 3 4c0-.6.4-1 1-1h3.5c.6 0 1 .4 1 1 0 1.3.2 2.5.6 3.6.1.3 0 .7-.2 1z"/></svg>
    555 208 4417
  </div>
</header>

<nav class="abs main-nav">
  <div class="abs nav-active"></div>
  <span class="nav-item" style="left:193px">Home</span>
  <span class="nav-item" style="left:342px">About Us</span>
  <span class="nav-item" style="left:502px">Services</span>
  <span class="nav-item" style="left:660px">Gallery</span>
  <span class="nav-item" style="left:815px">Reviews</span>
  <span class="nav-item" style="left:983px">Contact Us</span>
</nav>

<section class="abs hero" role="img" aria-label="Bright modern interior with dining table, armchairs and a dark wood floor"></section>
<div class="abs hero-caption">Maecenas vel<br>tortor accumsan</div>
<div class="abs hero-arrow" style="left:0"><svg width="10" height="10" viewBox="0 0 10 10"><path d="M7 1 3 5l4 4" stroke="#fff" stroke-width="2" fill="none"/></svg></div>
<div class="abs hero-arrow" style="right:0"><svg width="10" height="10" viewBox="0 0 10 10"><path d="M3 1l4 4-4 4" stroke="#fff" stroke-width="2" fill="none"/></svg></div>

<section>
  <h2 class="abs welcome-title">Welcome to<br>Harlow Custom Furniture</h2>
  <p class="abs body-copy welcome-copy">Aenean facilisis tincidunt lectus, id dictum nisi luctus eget. Vivamus efficitur ex condimentum, malesuada eros eget, feugiat nibh. Sed tellus ex, imperdiet eget gravida sit amet, volutpat eget turpis. In nec ultricies est. Etiam mattis augue vehicula odio posuere, sit amet tempus lectus luctus. Nulla facilisi. Etiam vel massa elementum, bibendum tellus venenatis, feugiat massa. Curabitur venenatis lacinia ornare.</p>
  <span class="abs btn" style="left:132px;top:948px">Read More</span>
  <div class="abs welcome-photo" role="img" aria-label="Craftsman routing a wooden board on a workbench"></div>
</section>

<section>
  <div class="abs service-band" style="left:0;width:601px;background:var(--band)"></div>
  <div class="abs service-band" style="left:601px;width:599px;background:var(--band-dark)"></div>

  <svg class="abs service-icon" style="left:132px;top:1143px" viewBox="0 0 64 64" role="img" aria-label="Workshop tools icon">
    <g fill="none" stroke="#333" stroke-width="2"><rect x="4" y="6" width="22" height="10"/><line x1="15" y1="16" x2="15" y2="60"/><rect x="32" y="6" width="10" height="54"/><rect x="48" y="6" width="10" height="54"/></g>
  </svg>
  <h2 class="abs service-title" style="left:220px;top:1136px">Custom<br>Workshop</h2>
  <p class="abs body-copy service-copy" style="left:132px;top:1235px">Aliquam erat volutpat. Quisque aliquet ex nec est vestibulum pulvinar. Pellentesque convallis molestie enim sit amet efficitur. Etiam id imperdiet lectus. Vivamus lacus justo, ultrices nec erat in, euismod iaculis mauris. Vivamus eleifend vitae nulla vel malesuada.</p>
  <span class="abs btn" style="left:132px;top:1356px">Read More</span>

  <svg class="abs service-icon" style="left:648px;top:1143px" viewBox="0 0 64 64" role="img" aria-label="Table and chairs icon">
    <g fill="none" stroke="#333" stroke-width="2"><rect x="16" y="22" width="32" height="6"/><line x1="32" y1="28" x2="32" y2="58"/><line x1="4" y1="8" x2="4" y2="58"/><line x1="4" y1="36" x2="14" y2="36"/><line x1="14" y1="36" x2="14" y2="58"/><line x1="60" y1="8" x2="60" y2="58"/><line x1="50" y1="36" x2="60" y2="36"/><line x1="50" y1="36" x2="50" y2="58"/></g>
  </svg>
  <h2 class="abs service-title" style="left:752px;top:1136px">Custom<br>Furniture</h2>
  <p class="abs body-copy service-copy" style="left:648px;top:1235px">Aliquam erat volutpat. Quisque aliquet ex nec est vestibulum pulvinar. Pellentesque convallis molestie enim sit amet efficitur. Etiam id imperdiet lectus. Vivamus lacus justo, ultrices nec erat in, euismod iaculis mauris. Vivamus eleifend vitae nulla vel malesuada.</p>
  <span class="abs btn" style="left:648px;top:1356px">Read More</span>
</section>

<section>
  <h2 class="abs gallery-title">Gallery</h2>
  <div class="tile" style="left:132px;top:1600px;width:223px;height:161px;background:linear-gradient(180deg,#9fb7c6,#6d7a55 45%,#5a4632)" role="img" aria-label="Wooden chairs on a terrace overlooking a lake"></div>
  <div class="tile" style="left:369px;top:1600px;width:222px;height:161px;background:linear-gradient(135deg,#efe9e4,#c9c1ba 50%,#7a3a26)" role="img" aria-label="Retail display shelving in red wood"></div>
  <div class="tile" style="left:608px;top:1600px;width:460px;height:161px;background:linear-gradient(160deg,#2a2624,#6b5d52 40%,#e2ddd6 70%,#b58a5e)" role="img" aria-label="Kitchen cabinetry during installation"></div>
  <div class="tile" style="left:132px;top:1776px;width:246px;height:170px;background:linear-gradient(135deg,#c98a4a,#f4f2ee 45%,#fafafa)" role="img" aria-label="White media unit with wood wall panel"></div>
  <div class="tile" style="left:380px;top:1776px;width:211px;height:170px;background:linear-gradient(135deg,#f6f4f0,#e9e3da 55%,#c59a62)" role="img" aria-label="Bright room with white chairs and wood cabinets"></div>
  <div class="tile" style="left:608px;top:1776px;width:223px;height:170px;background:linear-gradient(160deg,#e8e4df,#7a4a34 45%,#4a2d22)" role="img" aria-label="Leather sofa in a living room"></div>
  <div class="tile" style="left:842px;top:1776px;width:226px;height:170px;background:linear-gradient(160deg,#2b4d8e,#4b78b8 45%,#8a6a4a)" role="img" aria-label="Lounge seating with a blue feature wall"></div>
  <svg class="abs gallery-arrow" style="left:52px" viewBox="0 0 24 30"><path d="M16 5 6 15l10 10" stroke="#222" stroke-width="2.5" fill="none"/></svg>
  <svg class="abs gallery-arrow" style="left:1124px" viewBox="0 0 24 30"><path d="M8 5l10 10-10 10" stroke="#222" stroke-width="2.5" fill="none"/></svg>
</section>

<section>
  <div class="abs reviews"></div>
  <h2 class="abs reviews-title">Reviews</h2>
  <p class="abs quote">“ Etiam mattis augue vehicula odio posuere, sit amet tempus lectus luctus. Nulla facilisi. Etiam vel massa elementum, bibendum tellus venenatis, feugiat massa. Curabitur venenatis lacinia ornare. ”</p>
  <p class="abs reviewer">Martin Avery, City</p>
  <div class="abs dots"><span class="dot on"></span><span class="dot"></span><span class="dot"></span><span class="dot"></span></div>
</section>

<section>
  <h2 class="abs contact-title">Contact Us</h2>
  <div class="abs contact-item" style="left:132px">
    <svg width="10" height="14" viewBox="0 0 10 14"><path d="M5 0a5 5 0 0 0-5 5c0 4 5 9 5 9s5-5 5-9a5 5 0 0 0-5-5zm0 7a2 2 0 1 1 0-4 2 2 0 0 1 0 4z" fill="#222"/></svg>
    24 Building name, Street name, City Zipcode
  </div>
  <div class="abs contact-item" style="left:578px">
    <svg width="13" height="13" viewBox="0 0 24 24"><path fill="#222" d="M6.6 10.8c1.4 2.8 3.8 5.1 6.6 6.6l2.2-2.2c.3-.3.7-.4 1-.2 1.1.4 2.3.6 3.6.6.6 0 1 .4 1 1V20c0 .6-.4 1-1 1C10.6 21 3 13.4 3 4c0-.6.4-1 1-1h3.5c.6 0 1 .4 1 1 0 1.3.2 2.5.6 3.6.1.3 0 .7-.2 1z"/></svg>
    555 730 1926
  </div>
  <div class="abs contact-item" style="left:770px">
    <svg width="15" height="12" viewBox="0 0 15 12"><rect width="15" height="12" fill="#222"/><path d="M1 1l6.5 5L14 1" stroke="#fff" stroke-width="1.3" fill="none"/></svg>
    info@harlowcustomfurniture.com
  </div>
</section>

<footer class="abs site-footer"></footer>
<div class="abs footer-links" style="color:var(--white)">Home<span>|</span>About Us<span>|</span>Services<span>|</span>Gallery<span>|</span>Reviews<span>|</span>Contact Us</div>
<div class="abs copyright" style="color:var(--white)">Copyright © 2018 Harlow Custom Furniture. All rights reserved.</div>
<span class="abs social" style="left:975px" role="img" aria-label="Social link"></span>
<span class="abs social" style="left:1010px" role="img" aria-label="Social link"></span>
<span class="abs social" style="left:1049px" role="img" aria-label="Social link"></span>

</body>
</html>
```